Harlow Ridge Growers and Nursery needs a business street sign.

I have three businesses located at the same address: The Harlow Ridge Growers & Nursery, The Bramble Nook, and The Quarry Commons. I am looking for a 4’ x 8’ street sign to represent all three businesses as one retail experience. It needs to be eye catching yet simple enough that people can fully read it while driving by. I have logos for the greenhouse and village however I do not have anything for The Bramble Nook. I’m looking for some type of font that’s similar or in between the two attached logos for The Bramble Nook.

• Horizontal Sign, Eye catching, yet simple design so people see it while driving by.
• Horizontal Sign
• I’m open to the design being both vertical and horizontal. Please provide both options

```html
<!DOCTYPE html>
<html lang="en">
<head>
<meta charset="utf-8">
<title>Harlow Ridge Growers &amp; Nursery – Street Sign</title>
<link href="https://fonts.googleapis.com/css2?family=Cabin:wght@600;700&display=swap" rel="stylesheet">
<style>
  :root {
    --backdrop: #464648;
    --sign-white: #fdfcfb;
    --leaf-green: #1d7150;
    --wine: #7b2f32;
    --brick: #9a3a34;
    --blush: #f2a7b8;
    --rose: #e8708f;
    --peach: #fbd9a6;
    --sage: #8aa57a;
  }
  * { margin: 0; padding: 0; box-sizing: border-box; }
  html, body { width: 1200px; height: 969px; overflow: hidden; background: var(--backdrop); }
  .canvas { position: relative; width: 1200px; height: 969px; }
  .sign {
    position: absolute; left: 410px; top: 104px; width: 381px; height: 762px;
    background: var(--sign-white); overflow: hidden;
    box-shadow: 0 4px 14px rgba(0,0,0,.35);
    font-family: "Cabin", sans-serif;
  }
  .floral { position: absolute; border-radius: 50%; filter: blur(6px); }
  .floral-top-left { left: -50px; top: -40px; width: 190px; height: 210px;
    background: radial-gradient(circle at 55% 45%, var(--rose), var(--blush) 55%, rgba(242,167,184,0) 75%); }
  .floral-top-right { left: 170px; top: -60px; width: 260px; height: 290px;
    background: radial-gradient(circle at 70% 30%, var(--rose) 0, var(--peach) 45%, rgba(251,217,166,0) 72%); }
  .floral-right-sprig { left: 320px; top: 230px; width: 80px; height: 110px;
    background: radial-gradient(circle, var(--blush), rgba(242,167,184,0) 70%); }
  .floral-left-sprig { left: -30px; top: 190px; width: 70px; height: 130px;
    background: radial-gradient(circle, var(--peach), rgba(251,217,166,0) 70%); }
  .floral-mid-right { left: 320px; top: 460px; width: 80px; height: 110px;
    background: radial-gradient(circle, var(--peach), rgba(251,217,166,0) 70%); }
  .floral-bottom-left { left: -70px; top: 560px; width: 260px; height: 260px;
    background: radial-gradient(circle at 45% 60%, var(--rose), var(--blush) 50%, rgba(138,165,122,.4) 68%, rgba(242,167,184,0) 76%); }
  .floral-bottom-right { left: 300px; top: 650px; width: 120px; height: 150px;
    background: radial-gradient(circle, var(--rose), rgba(242,167,184,0) 70%); }

  .business { position: absolute; left: 0; width: 100%; text-align: center; }
  .business-name { font-weight: 700; line-height: 1.02; }
  .growers { top: 150px; }
  .growers .business-name { color: var(--leaf-green); font-size: 44px; }
  .tagline {
    display: inline-block; margin-top: 8px; padding: 3px 12px;
    background: var(--wine); color: #f6e7dc; font-weight: 600; font-size: 14px;
    letter-spacing: .3px; border-radius: 3px;
  }
  .nook { top: 335px; }
  .nook .business-name { color: var(--leaf-green); font-size: 52px; }
  .nook .tagline { font-size: 20px; padding: 1px 14px; }
  .commons { top: 545px; }
  .commons .business-name { color: var(--brick); font-size: 48px; }
</style>
</head>
<body>
<div class="canvas">
  <section class="sign" aria-label="Street sign for three businesses">
    <div class="floral floral-top-left" role="img" aria-label="Watercolour pink blossoms and leaves"></div>
    <div class="floral floral-top-right" role="img" aria-label="Watercolour peach lily and pink petals"></div>
    <div class="floral floral-left-sprig" role="img" aria-label="Faint yellow watercolour sprig"></div>
    <div class="floral floral-right-sprig" role="img" aria-label="Small pink watercolour petals"></div>
    <div class="floral floral-mid-right" role="img" aria-label="Faint yellow watercolour buds"></div>
    <div class="floral floral-bottom-left" role="img" aria-label="Watercolour pink peony with green leaves"></div>
    <div class="floral floral-bottom-right" role="img" aria-label="Watercolour pink petal"></div>

    <div class="business growers">
      <p class="business-name">The Harlow<br>Ridge</p>
      <p class="tagline">GROWERS &amp; NURSERY</p>
    </div>
    <div class="business nook">
      <p class="business-name">The Bramble<br>Nook</p>
    </div>
    <div class="business commons">
      <p class="business-name">Quarry<br>Commons</p>
    </div>
  </section>
</div>
</body>
</html>
```